Flyer Template Design

I have attached 4 files. I would like a design template that could be used across these documents so that they have a common look and feel. The content of the documents is tested and should not be changed significantly. The images can be changed. I have also attache our logo for color compatibility.
Updates

Need extra days to review

Target Market(s)

Wealthy Christian donors

Font styles to use
Serif
Sans Serif

```html
<!DOCTYPE html>
<html lang="en">
<head>
<meta charset="utf-8">
<title>Finishing the Great Commission</title>
<link href="https://fonts.googleapis.com/css2?family=Lato:wght@300;400;700;900&display=swap" rel="stylesheet">
<style>
  :root {
    --cyan: #7ffcfc;
    --lime: #95f244;
    --ink: #1e1e1e;
    --white: #ffffff;
    --backdrop: #f2f2f2;
    --photo-pink: #c8326a;
    --photo-green: #4f6a2e;
  }
  html, body {
    margin: 0;
    width: 1200px;
    height: 1200px;
    overflow: hidden;
    background: var(--backdrop);
  }
  .flyer {
    position: absolute;
    left: 193px;
    top: 25px;
    width: 956px;
    height: 1352px;
    background: var(--white);
    transform: scale(0.85);
    transform-origin: 0 0;
    overflow: hidden;
    font-family: "Lato", Arial, sans-serif;
    color: var(--ink);
  }
  .header-shapes, .footer-shapes {
    position: absolute;
    left: 0;
    top: 0;
    width: 956px;
    height: 1352px;
  }
  .title {
    position: absolute;
    left: 58px;
    top: 52px;
    margin: 0;
    font-weight: 300;
    font-size: 44px;
    line-height: 52px;
    color: var(--white);
    letter-spacing: 0.5px;
  }
  .hero-photo {
    position: absolute;
    left: 588px;
    top: 19px;
    width: 304px;
    height: 384px;
    border: 4px solid var(--white);
    background: radial-gradient(circle at 55% 50%, var(--photo-pink) 0 40%, #7a2a30 60%, var(--photo-green) 100%);
  }
  .body-text {
    position: absolute;
    left: 58px;
    font-size: 16.5px;
    line-height: 21.3px;
    font-weight: 400;
    margin: 0;
  }
  .intro { top: 328px; width: 530px; }
  .section-head {
    font-weight: 400;
    font-size: 17px;
    text-transform: uppercase;
    display: block;
  }
  .nations { top: 475px; width: 840px; }
  .stand { top: 602px; width: 840px; }
  .callout {
    position: absolute;
    left: 58px;
    top: 731px;
    margin: 0;
    font-size: 24px;
    font-weight: 900;
    color: var(--cyan);
  }
  .hasten { top: 782px; width: 690px; }
  .cta-headline {
    position: absolute;
    left: 58px;
    top: 914px;
    margin: 0;
    font-size: 42px;
    font-weight: 900;
    color: var(--lime);
    letter-spacing: 0.3px;
  }
  .partner { top: 1004px; width: 690px; }
  .contact { top: 1110px; width: 690px; }
  .brand {
    position: absolute;
    left: 718px;
    top: 1210px;
    display: flex;
    align-items: center;
    gap: 12px;
  }
  .brand-mark {
    width: 30px;
    height: 30px;
    background: var(--lime);
  }
  .brand-name {
    font-family: "Lato", Arial, sans-serif;
    font-weight: 700;
    font-size: 17px;
    line-height: 18px;
    color: var(--ink);
    text-transform: uppercase;
  }
</style>
</head>
<body>
  <main class="flyer">
    <svg class="header-shapes" viewBox="0 0 956 1352" aria-hidden="true">
      <polygon points="0,0 956,0 956,85 588,140 255,187 0,320" fill="var(--cyan)"/>
      <polygon points="0,320 255,187 588,140 588,172 235,265 0,350" fill="var(--lime)"/>
    </svg>
    <svg class="footer-shapes" viewBox="0 0 956 1352" aria-hidden="true">
      <polygon points="505,1352 660,1148 956,1082 956,1086 680,1148 520,1352" fill="var(--cyan)"/>
      <polygon points="520,1352 680,1148 956,1086 956,1090 700,1148 532,1352" fill="var(--lime)"/>
    </svg>

    <h1 class="title">FINISHING THE<br>GREAT COMMISSION</h1>

    <div class="hero-photo" role="img" aria-label="Portrait photo of a smiling woman wearing a bright pink head scarf"></div>

    <p class="body-text intro">Before Jesus ascended into heaven, He commanded his apostles, “Go and make disciples of all nations.” For more than 2000 years the church has been working to fulfill this “Great Commission,” and much has been accomplished. But now, for the first time in history, our generation has the real opportunity to finish the Great Commission in our lifetimes.</p>

    <p class="body-text nations"><span class="section-head">It’s about nations</span>In the Bible, the word “nations” refers to people groups: groups of people who share a common ethnicity, culture, and language. So when Jesus said, “Go and make disciples if all nations,” He was telling us to take the gospel to every people group on earth. Amazingly, there are about 12,000 of these people groups scattered throughout the world. And the Great Commission commands us to make disciples in every one of them.</p>

    <p class="body-text stand"><span class="section-head">Where do we stand?</span>Today, there are still about 500 people groups who have never heard the gospel. Most of these groups are small and located in remote, difficult places. These remaining “unengaged” people groups have no known believers. But now that we know who and where these groups are, by God’s grace it is possible that we can engage every one of them with the gospel within the next 3 years.</p>

    <p class="callout">In other words, we can finish the Great Commission!</p>

    <p class="body-text hasten"><span class="section-head">Hastening his coming</span>The Bible says that believers “ought to live holy and godly lives, looking for and hastening the coming of the day of God.” It also says that day will not come until the gospel has been preached to “all nations.” So how can hasten the day of his coming? By finishing the work he gave us to do: making disciples in all nations.</p>

    <h2 class="cta-headline">YOU CAN MAKE THAT HAPPEN.</h2>

    <p class="body-text partner">Partner with the Harvest Reach Fund and finance the missionaries who are taking the gospel for the first time to those last remaining people groups. Your investment will “hasten the coming of the day of God” by accelerating the effort to make “disciples in every nation.” In 2018, our partners helped take the gospel to 231 people groups in 35 countries.</p>

    <p class="body-text contact">Join us as we invest to make disciples in “all nations” by 2022.<br>To learn more, email Daniel Hale at dhale@harvestreach.org.</p>

    <div class="brand">
      <span class="brand-mark"></span>
      <span class="brand-name">The Harvest<br>Reach Fund</span>
    </div>
  </main>
</body>
</html>
```